Tech business card design

We need an amazing business card design for our new business 'Brakka' a marketing tech startup based in Sydney, Australia. We provide an online marketplace for businesses to search and buy advertising media, connect with service providers and learn more about marketing. We wish to communicate 'cool tech', reliability and professionalism and design based around our logo.

Target Market(s)

Business Owners

Contact Information for Business Card

Name
Position
Email Address
Website
Phone Number

Font styles to use
Other font styles liked:
• Avenir & Avenir Next

Colors

Designer to choose colors to be used in the design.

```html
<!DOCTYPE html>
<html lang="en">
<head>
<meta charset="utf-8">
<title>Brakka Business Card</title>
<link rel="stylesheet" href="https://fonts.googleapis.com/css2?family=Montserrat:wght@400;500;800&display=swap">
<style>
  :root {
    --page-bg: #3a3a3c;
    --navy-deep: #0a0b24;
    --navy-mid: #1c1d5a;
    --indigo-glow: #2f2c9e;
    --ink: #14163a;
    --ink-soft: #4a4b5e;
    --paper: #ffffff;
    --logo-light: #eef0f6;
  }
  * { margin: 0; padding: 0; box-sizing: border-box; }
  html, body {
    width: 1200px; height: 1000px; overflow: hidden;
    background: var(--page-bg);
    font-family: "Montserrat", sans-serif;
  }
  .card {
    position: absolute; left: 250px;
    width: 700px; height: 400px;
    border-radius: 26px; overflow: hidden;
    box-shadow: 0 14px 30px rgba(0,0,0,.35);
  }
  .card-front { top: 60px; background: var(--navy-deep); }
  .front-texture {
    position: absolute; inset: 0;
    background: radial-gradient(ellipse at 55% 50%, var(--indigo-glow) 0%, var(--navy-mid) 35%, var(--navy-deep) 75%);
  }
  .wordmark {
    position: absolute; display: inline-block;
    font-weight: 800; line-height: 1; letter-spacing: -2px;
    white-space: nowrap;
  }
  .wordmark .tm {
    position: absolute; right: -24px; bottom: -4px;
    font-size: 13px; letter-spacing: 0;
  }
  .front-wordmark {
    left: 50%; top: 140px; transform: translateX(-50%);
    font-size: 104px; color: var(--logo-light);
  }
  .card-back { top: 540px; background: var(--paper); }
  .back-wordmark {
    left: 36px; top: 163px;
    font-size: 66px; color: var(--ink);
  }
  .back-wordmark .tm { right: -20px; bottom: -6px; font-size: 10px; }
  .divider {
    position: absolute; left: 325px; top: 110px;
    width: 2px; height: 180px; background: var(--ink);
  }
  .contact { position: absolute; left: 350px; top: 112px; color: var(--ink); }
  .person-name { font-size: 26px; font-weight: 500; }
  .person-role { font-size: 15px; color: var(--ink-soft); margin-bottom: 22px; }
  .contact-list { list-style: none; }
  .contact-list li {
    display: flex; align-items: center; gap: 10px;
    font-size: 17px; font-weight: 500; margin-bottom: 8px;
  }
  .contact-list svg { width: 22px; height: 22px; flex: none; }
</style>
</head>
<body>
  <section class="card card-front">
    <div class="front-texture" role="img" aria-label="Dark blue abstract circuit-like tech texture"></div>
    <div class="wordmark front-wordmark">brakka<span class="tm">TM</span></div>
  </section>

  <section class="card card-back">
    <div class="wordmark back-wordmark">brakka<span class="tm">TM</span></div>
    <div class="divider"></div>
    <div class="contact">
      <p class="person-name">Marcus Hale</p>
      <p class="person-role">Managing Director</p>
      <ul class="contact-list">
        <li>
          <svg viewBox="0 0 22 22"><circle cx="11" cy="11" r="10" fill="none" stroke="#14163a" stroke-width="1.5"/><rect x="8" y="5.5" width="6" height="11" rx="1.2" fill="none" stroke="#14163a" stroke-width="1.4"/></svg>
          800-555-0142
        </li>
        <li>
          <svg viewBox="0 0 22 22"><circle cx="11" cy="11" r="10" fill="none" stroke="#14163a" stroke-width="1.5"/><rect x="6" y="7.5" width="10" height="7" fill="none" stroke="#14163a" stroke-width="1.4"/><path d="M6 7.5l5 4 5-4" fill="none" stroke="#14163a" stroke-width="1.4"/></svg>
          marcus@brakkamail.com
        </li>
        <li>
          <svg viewBox="0 0 22 22"><circle cx="11" cy="11" r="10" fill="none" stroke="#14163a" stroke-width="1.5"/><circle cx="11" cy="11" r="6" fill="none" stroke="#14163a" stroke-width="1.3"/><path d="M5 11h12M11 5c-3 3-3 9 0 12M11 5c3 3 3 9 0 12" fill="none" stroke="#14163a" stroke-width="1.2"/></svg>
          www.brakka.com
        </li>
      </ul>
    </div>
  </section>
</body>
</html>
```